Beauty Therapy Web Design

I need a web page design for a small beauty therapy clinic, the owner is currently the only beauty therapist working there.
We require the following pages:
Home
About
Treatments
Nails
Courses
Contact
I will attach the clinics business card, treatment menu and signage so that you get a feeling for the branding colours etc.
This is the first website for the beauty therapist, she would like to attract new clients and also tourists that come in on the cruise ships. The thing that sets her apart from other clinics is that she welcomes texting for appointments.
I have selected refundable because I have never done this before so I don't know what to expect, I have the full intention of going through with it as long as I get a good design.
Feel free to ask for further information
Reason: Project extended as I am away for work and am unable to meet with the owner.
Target Market(s)
Females 18 to 50
Industry/Entity Type
Business
Look and feel
Each slider illustrates characteristics of the customer's brand and the style your logo design should communicate.

```html
<!DOCTYPE html>
<html lang="en">
<head>
<meta charset="utf-8">
<title>Lumina Beauty Therapy – Treatments</title>
<link rel="stylesheet" href="https://fonts.googleapis.com/css2?family=Tinos:ital,wght@0,400;0,700;1,700&family=Arimo:wght@400;700&display=swap">
<style>
  :root {
    --page-purple: #6a57a2;
    --page-purple-deep: #574491;
    --glow: rgba(255, 255, 255, 0.55);
    --gold: #c7a548;
    --gold-deep: #a8862c;
    --tab-cream: #f1e6b4;
    --tab-text: #6b5a1e;
    --tab-active-text: #c4561a;
    --card-lilac: #dedbe7;
    --panel-purple: #6c59a4;
    --panel-edge: #7d6659;
    --button-top: #fff6d8;
    --button-bottom: #f3d79a;
    --button-edge: #d9a85a;
    --button-text: #a5501c;
    --white: #ffffff;
  }
  * { box-sizing: border-box; margin: 0; padding: 0; }
  html, body { width: 1200px; height: 990px; overflow: hidden; }
  body {
    position: relative;
    font-family: "Arimo", Arial, sans-serif;
    background:
      radial-gradient(ellipse 120px 80px at 310px 0, var(--glow), transparent 70%),
      radial-gradient(ellipse 120px 80px at 890px 0, var(--glow), transparent 70%),
      radial-gradient(ellipse 500px 160px at 600px 20px, rgba(255,255,255,0.18), transparent 70%),
      linear-gradient(180deg, var(--page-purple) 0%, var(--page-purple-deep) 100%);
  }

  .brand {
    position: absolute; left: 0; top: 4px; width: 1200px;
    text-align: center; color: var(--gold);
    font-family: "Tinos", "Times New Roman", serif; font-weight: 400;
  }
  .brand-name { font-size: 84px; line-height: 92px; }
  .brand-sub { font-size: 56px; line-height: 60px; }
  .brand-phone {
    position: absolute; left: 0; top: 184px; width: 1200px;
    text-align: center; color: var(--gold);
    font-family: "Tinos", "Times New Roman", serif; font-weight: 700; font-size: 26px;
  }

  .site-frame {
    position: absolute; left: 106px; top: 226px; width: 1000px; height: 744px;
    border: 2px solid var(--gold); border-radius: 7px; overflow: hidden;
  }
  .tab-bar {
    position: absolute; left: 0; top: 0; width: 100%; height: 44px;
    border-bottom: 3px solid var(--gold);
  }
  .tab {
    position: absolute; top: 14px; height 28px; height: 28px;
    background: var(--tab-cream); color: var(--tab-text);
    border: 1px solid var(--gold); border-bottom: none;
    border-radius: 6px 6px 0 0;
    font-size: 13.5px; line-height: 27px; text-align: center; text-decoration: none;
  }
  .tab.is-active { background: var(--white); color: var(--tab-active-text); }

  .page-body {
    position: absolute; left: 0; top: 44px; width: 100%; height: 663px;
    background: var(--white);
  }
  .hero {
    position: absolute; left: 1px; top: 2px; width: 995px; height: 345px;
    background:
      radial-gradient(ellipse 260px 160px at 250px 130px, #8a4a2a, transparent 70%),
      radial-gradient(ellipse 300px 130px at 700px 150px, #d9a888, transparent 70%),
      linear-gradient(180deg, #b98a6e 0%, #e8d6c8 55%, #ffffff 100%);
  }

  .treatment-card {
    position: absolute; top: 356px; width: 236px; height: 296px;
    background: var(--card-lilac);
  }
  .treatment-panel {
    position: absolute; left: 31px; top: 32px; width: 175px; height: 192px;
    background: var(--panel-purple);
    border: 3px solid var(--panel-edge); border-radius: 32px;
    box-shadow: 3px 4px 5px rgba(60, 40, 40, 0.45);
  }
  .treatment-title {
    position: absolute; left: 0; top: 18px; width: 100%;
    text-align: center; color: var(--gold);
    font-family: "Tinos", "Times New Roman", serif; font-style: italic; font-weight: 700;
    font-size: 20px;
  }
  .treatment-photo {
    position: absolute; left: 13px; top: 64px; width: 143px; height: 89px;
  }
  .learn-more {
    position: absolute; left: 73px; top: 256px; width: 90px; height: 27px;
    background: linear-gradient(180deg, var(--button-top), var(--button-bottom));
    border: 1px solid var(--button-edge); border-radius: 3px;
    box-shadow: 1px 2px 2px rgba(0,0,0,0.25);
    color: var(--button-text); font-size: 12.5px; line-height: 25px;
    text-align: center; text-decoration: none;
  }

  .site-footer {
    position: absolute; left: 0; top: 707px; width: 100%; height: 37px;
    background: var(--page-purple); color: var(--white);
    text-align: center; font-size: 11.5px; font-weight: 700; line-height: 14px;
    padding-top: 4px;
  }
  .site-footer a { color: var(--white); text-decoration: none; }
</style>
</head>
<body>
  <header class="brand">
    <div class="brand-name">Lumina</div>
    <div class="brand-sub">Beauty Therapy</div>
  </header>
  <div class="brand-phone">Phone: 07 555 0182</div>

  <div class="site-frame">
    <nav class="tab-bar">
      <a class="tab" href="#" style="left:4px;width:68px">Home</a>
      <a class="tab" href="#" style="left:79px;width:89px">About Us</a>
      <a class="tab is-active" href="#" style="left:173px;width:99px">Treatments</a>
      <a class="tab" href="#" style="left:278px;width:64px">Nails</a>
      <a class="tab" href="#" style="left:348px;width:84px">Courses</a>
      <a class="tab" href="#" style="left:438px;width:99px">Contact Us</a>
    </nav>

    <main class="page-body">
      <div class="hero" role="img" aria-label="Photo of a relaxing back massage with a lit candle and spa decor"></div>

      <section class="treatment-card" style="left:9px">
        <div class="treatment-panel">
          <h2 class="treatment-title">Waxing</h2>
          <div class="treatment-photo" role="img" aria-label="Photo of a wax bowl with honey and marigold flowers" style="background:linear-gradient(180deg,#f3efe8 0%,#c97a2a 55%,#e89a1e 100%)"></div>
        </div>
        <a class="learn-more" href="#">Learn More</a>
      </section>

      <section class="treatment-card" style="left:256px">
        <div class="treatment-panel">
          <h2 class="treatment-title">Nails</h2>
          <div class="treatment-photo" role="img" aria-label="Photo of manicured hands and feet with orchids" style="background:linear-gradient(180deg,#8b4f8f 0%,#e0b89c 50%,#caa086 100%)"></div>
        </div>
        <a class="learn-more" href="#">Learn More</a>
      </section>

      <section class="treatment-card" style="left:503px">
        <div class="treatment-panel">
          <h2 class="treatment-title">Facials</h2>
          <div class="treatment-photo" role="img" aria-label="Photo of a client receiving a facial treatment" style="background:linear-gradient(135deg,#6a4a3c 0%,#c9967a 50%,#efe6df 100%)"></div>
        </div>
        <a class="learn-more" href="#">Learn More</a>
      </section>

      <section class="treatment-card" style="left:749px">
        <div class="treatment-panel">
          <h2 class="treatment-title">Body Treatments</h2>
          <div class="treatment-photo" role="img" aria-label="Photo of spa oils, towels and bamboo mat" style="background:linear-gradient(180deg,#6b3e1e 0%,#b8803e 50%,#e8d8c0 100%)"></div>
        </div>
        <a class="learn-more" href="#">Learn More</a>
      </section>
    </main>

    <footer class="site-footer">
      <a href="#">Home</a> | <a href="#">About Us</a> |<a href="#">Treatments</a> | <a href="#">Nails</a> | <a href="#">Courses</a> | <a href="#">Contact Us</a><br>
      Copyright © 2011. All Rights Reserved.
    </footer>
  </div>
</body>
</html>
```